Tidal Forge MSP - Power Point Template Creation

I need someone to create a full slide deck template that is branded with logo and follows our color choices that can be used as a template to create presentations from.

```html
<!DOCTYPE html>
<html lang="en">
<head>
<meta charset="utf-8">
<title>Tidal Forge MSP – Slide Deck Template</title>
<link rel="stylesheet" href="https://fonts.googleapis.com/css2?family=Montserrat:ital,wght@0,300;0,400;0,500;0,600;0,700;0,800;1,500&family=Roboto:wght@300;400&display=swap">
<style>
:root{
  --bg:#e5e5e3;
  --paper:#ffffff;
  --ink:#1e1e1e;
  --dark:#2a2a2a;
  --muted:#8c8c8c;
  --gold:#b8893a;
  --gold-dark:#9a6a24;
  --gold-light:#d8b66a;
  --gold-grad:linear-gradient(120deg,#8a5a1c 0%,#c39a45 38%,#efdc98 62%,#b5822d 100%);
  --gold-grad-v:linear-gradient(180deg,#efdc98 0%,#c39a45 45%,#8a5a1c 100%);
  --gold-grad-h:linear-gradient(90deg,#efdc98 0%,#c9a24a 50%,#9a6a24 100%);
}
*{box-sizing:border-box;margin:0;padding:0}
html,body{width:1044px;height:1200px;overflow:hidden}
body{background:var(--bg);font-family:"Montserrat",sans-serif;color:var(--ink)}
.slide{position:absolute;width:308px;height:174px;background:var(--paper);overflow:hidden;box-shadow:1px 2px 5px rgba(0,0,0,.22)}
.a{position:absolute}
.gold{background:var(--gold-grad)}
.gold-v{background:var(--gold-grad-v)}
.gold-h{background:var(--gold-grad-h)}
.photo{position:absolute}
.pg{position:absolute;right:8px;bottom:6px;font-size:4px;color:#555}
.h{font-weight:800;line-height:1.12;color:var(--ink)}
.h .hl{color:var(--gold)}
.tiny{font-size:3.5px;line-height:1.4;color:var(--muted)}
.tiny-w{font-size:3.3px;line-height:1.35;color:#fff}
.rule{position:absolute;height:1.4px;width:14px;background:var(--gold)}
.rule::after{content:"";position:absolute;left:16px;top:0;width:4px;height:1.4px;background:var(--gold-light)}
.logo{font-family:"Montserrat",sans-serif;font-weight:400;font-size:7px;color:var(--ink);letter-spacing:.3px;display:flex;align-items:center;gap:3px;white-space:nowrap}
.logo-dot{width:5px;height:5px;background:var(--gold);display:inline-block}
svg{position:absolute;left:0;top:0;overflow:visible}
/* cover */
.cover-title{font-family:"Roboto",sans-serif;font-weight:300;font-size:19px;line-height:1;letter-spacing:.2px}
.cover-sub{font-weight:700;font-size:11px;letter-spacing:.3px}
.dots span{display:inline-block;width:3px;height:3px;border-radius:50%;background:var(--gold);margin-right:2px}
/* agenda */
.agenda-item{position:absolute;left:165px;width:125px}
.agenda-item b{display:block;font-size:6px;font-weight:600;margin-bottom:1px}
/* cards */
.card{position:absolute;width:61px;height:77px;background:#fff;box-shadow:0 1px 3px rgba(0,0,0,.25)}
.card-head{height:22px;color:#fff;font-weight:700;font-size:9px;display:flex;align-items:center;justify-content:center}
.card .tiny{padding:3px 4px;font-size:2.9px}
/* numbered panels */
.num-list{position:absolute;color:#fff}
.num-row{position:absolute;left:6px;display:flex;gap:4px}
.num-box{width:10px;height:10px;background:var(--dark);color:#fff;font-weight:800;font-size:7px;display:flex;align-items:center;justify-content:center;flex:none;border:.6px solid #fff}
.num-row b{display:block;font-size:5px;font-weight:700;color:#fff;margin-bottom:.5px}
/* icon rows */
.icon-row{position:absolute;display:flex;gap:7px;align-items:flex-start}
.icon-row b{display:block;font-size:6.5px;font-weight:600;margin-bottom:1px}
.icon-row .tiny{width:95px;color:#777}
/* swot */
.swot-label{position:absolute;font-size:4px;font-weight:600;font-style:italic;color:var(--ink)}
.swot-label ul{list-style:none;font-size:2.6px;font-weight:400;font-style:normal;color:#777;margin-top:2px;line-height:1.5}
/* timeline */
.tl-label{position:absolute;width:60px;text-align:center;font-size:4.2px;font-weight:600;transform:translateX(-50%)}
.tl-label span{display:block;font-weight:400;color:#777;font-size:3.4px;line-height:1.3}
/* buttons */
.btn{position:absolute;left:60px;width:109px;height:30px;color:#5a3c12;font-weight:700;font-size:9px;display:flex;align-items:center;padding-left:14px;box-shadow:2px 2px 4px rgba(0,0,0,.3)}
/* steps */
.step{position:absolute;width:46px;text-align:center;transform:translateX(-50%)}
.step b{display:block;font-size:5.5px;font-weight:600;margin-bottom:1px}
.step .tiny{font-size:2.6px;color:#777}
/* phones */
.phone{position:absolute;width:37px;height:78px;border:1.6px solid var(--dark);border-radius:4px;background:#fff;padding:10px 3px 3px}
.phone::before{content:"";position:absolute;left:12px;top:0;width:11px;height:2.5px;background:var(--dark);border-radius:0 0 2px 2px}
.phone b{display:block;font-size:4px;font-weight:600;line-height:1.2;margin-bottom:3px}
.phone .tiny{font-size:2.4px;color:#555}
.phone i{display:block;width:8px;height:8px;border:.8px solid var(--gold);border-radius:50%;margin:3px auto}
/* team */
.member{position:absolute;width:52px;text-align:center;transform:translateX(-50%)}
.avatar{width:25px;height:25px;border-radius:50%;margin:0 auto 4px;border:1.5px solid #fff;box-shadow:0 1px 2px rgba(0,0,0,.3);background:radial-gradient(circle at 50% 40%,#c9a385,#6b4c3b 70%,#e8e8e8 72%)}
.member b{display:block;font-size:5px;font-weight:700;margin-bottom:1.5px}
.member .tiny{font-size:2.6px;color:#777}
/* contact */
.contact{position:absolute;left:26px;display:flex;align-items:center;gap:4px;font-family:"Roboto",sans-serif;font-size:4px;line-height:1.35;color:#555}
.contact .sep{width:.7px;height:9px;background:#555}
</style>
</head>
<body>

<!-- 1 Cover -->
<section class="slide" style="left:47px;top:42px">
  <span class="a" style="left:6px;top:6px;width:7px;height:7px;background:var(--gold-light)"></span>
  <div class="a logo" style="left:17px;top:38px"><span class="logo-dot"></span>Tidal Forge MSP</div>
  <div class="a" style="left:18px;top:81px">
    <div class="cover-title">BUSINESS</div>
    <div class="cover-sub">MARKETING</div>
  </div>
  <div class="rule" style="left:18px;top:116px"></div>
  <div class="a" style="left:18px;top:120px;font-size:7px;font-style:italic;font-weight:500">Presentation</div>
  <div class="a tiny" style="left:18px;top:129px;width:82px;font-style:italic;color:#555">Lorem ipsum dolor sit amet, consectetuer adipiscing elit, sed diam nonum</div>
  <div class="a dots" style="left:18px;top:150px"><span></span><span></span><span></span></div>
  <div class="photo" role="img" aria-label="Photo of two colleagues reviewing work at a laptop in an office" style="left:129px;top:0;width:179px;height:141px;background:linear-gradient(135deg,#dfe5ea 0%,#8c96a0 45%,#3b4048 100%)"></div>
  <div class="a gold" style="left:129px;top:141px;width:179px;height:33px;display:flex;align-items:center;justify-content:center;color:#fff;font-size:5.5px;letter-spacing:2.5px;font-weight:500">WWW.<b style="font-weight:800">TIDALFORGE</b>.COM</div>
</section>

<!-- 2 Agenda -->
<section class="slide" style="left:372px;top:42px">
  <div class="photo" role="img" aria-label="Photo of a team meeting in a bright office" style="left:42px;top:0;width:108px;height:174px;background:linear-gradient(160deg,#f1f3f5 0%,#b8c1c9 45%,#5b5048 100%)"></div>
  <div class="a gold-v" style="left:26px;top:26px;width:32px;height:122px;display:flex;align-items:center;justify-content:center">
    <span style="writing-mode:vertical-rl;color:#fff;font-weight:800;font-size:15px;letter-spacing:.5px">Agenda</span>
  </div>
  <div class="agenda-item" style="top:38px"><b>1. Lorem ipsum</b><p class="tiny">Lorem ipsum dolor sit amet, consectetuer adipiscing elit, sed diam nonummy nibh euismod tincid</p></div>
  <div class="agenda-item" style="top:66px"><b>2. Lorem ipsum</b><p class="tiny">Lorem ipsum dolor sit amet, consectetuer adipiscing elit, sed diam nonummy nibh euismod tincid</p></div>
  <div class="agenda-item" style="top:95px"><b>3. Lorem ipsum</b><p class="tiny">Lorem ipsum dolor sit amet, consectetuer adipiscing elit, sed diam nonummy nibh euismod tincid</p></div>
  <div class="agenda-item" style="top:122px"><b>4. Lorem ipsum</b><p class="tiny">Lorem ipsum dolor sit amet, consectetuer adipiscing elit, sed diam nonummy nibh euismod tincid</p></div>
  <span class="a gold-v" style="left:303px;top:29px;width:4px;height:117px"></span>
  <span class="pg">2</span>
</section>

<!-- 3 Text Added Here -->
<section class="slide" style="left:696px;top:42px">
  <span class="a gold-v" style="left:0;top:48px;width:7px;height:86px"></span>
  <div class="a h" style="left:17px;top:54px;font-size:19px;line-height:24px">Text<br><span class="hl">Added</span><br>Here</div>
  <div class="photo" role="img" aria-label="Photo of hands working over charts and a laptop" style="left:98px;top:28px;width:210px;height:84px;background:linear-gradient(120deg,#2a3d6a 0%,#8ea4c4 50%,#dfe6ef 100%)"></div>
  <div class="card" style="left:137px;top:81px"><div class="card-head gold">Text Here</div><p class="tiny">Lorem ipsum dolor sit amet, consectetuer adipiscing elit, sed diam nonummy nibh euismod tincidunt ut laoreet dolore magna aliquam erat volutpat.<br><br>Ut wisi enim ad minim veniam, quis nostrud exerci tation ullamcorper suscipit lobortis nisl ut aliquip ex ea commodo conse</p></div>
  <div class="card" style="left:214px;top:81px"><div class="card-head gold">Text Here</div><p class="tiny">Lorem ipsum dolor sit amet, consectetuer adipiscing elit, sed diam nonummy nibh euismod tincidunt ut laoreet dolore magna aliquam erat volutpat.<br><br>Ut wisi enim ad minim veniam, quis nostrud exerci tation ullamcorper suscipit lobortis nisl ut aliquip ex ea commodo conse</p></div>
  <span class="pg">3</span>
</section>

<!-- 4 Lorem Ipsum -->
<section class="slide" style="left:47px;top:228px">
  <span class="a gold-v" style="left:0;top:0;width:8px;height:174px"></span>
  <span class="a gold" style="left:242px;top:0;width:66px;height:70px"></span>
  <span class="a gold-v" style="left:136px;top:102px;width:78px;height:72px"></span>
  <div class="a h" style="left:29px;top:36px;font-size:10.5px;letter-spacing:.6px;line-height:13px">Lorem Ipsum<br>Dolor Sit<br>Ametkeeper.</div>
  <div class="rule" style="left:29px;top:78px"></div>
  <p class="a tiny" style="left:29px;top:84px;width:96px">Lorem ipsum dolor sit amet, consectetuer adipiscing elit, sed diam nonummy nibh euismod tincidunt ut laoreet dolore magna aliquam erat volutpat. Ut wisi it lob edo consequat. Duis autem lore te feugait nulla facilisi.</p>
  <p class="a tiny" style="left:29px;top:118px;width:96px">Lorem ipsum dolor sit amet, cons ectetuer adipiscing elit, sed diam nonim ad minim veniam, quis nostrud exerci tation ullamcorper</p>
  <div class="photo" role="img" aria-label="Photo of a person lying on autumn leaves" style="left:150px;top:31px;width:138px;height:110px;background:linear-gradient(135deg,#5a3a26 0%,#8b5a36 40%,#2c2420 100%)"></div>
  <span class="pg">4</span>
</section>

<!-- 5 Part One -->
<section class="slide" style="left:372px;top:228px">
  <span class="a gold-v" style="left:0;top:0;width:7px;height:174px"></span>
  <div class="a h" style="left:28px;top:61px;font-size:13px">Part One</div>
  <p class="a tiny" style="left:28px;top:79px;width:96px">Lorem ipsum dolor sit amet, laoreet dolore magna aliquam erat volutpat. Ut wisi it lob edo consequat. Duis autem lore te feugait nulla facilisi.</p>
  <p class="a tiny" style="left:28px;top:98px;width:96px">Lorem ipsum dolor sit amet, cons ectetuer adipiscing elit, sed diam nonim ad minim veniam, quis nostrud exerci tation ullamcorper</p>
  <div class="photo" role="img" aria-label="Photo of hands holding a glowing light bulb" style="left:168px;top:15px;width:120px;height:143px;background:radial-gradient(circle at 60% 55%,#e8c878 0%,#6b5a3c 30%,#1e2326 70%)"></div>
  <div class="a gold" style="left:137px;top:52px;width:68px;height:69px;display:flex;align-items:center;justify-content:center;color:#fff;font-weight:800;font-size:40px;letter-spacing:-1px">01</div>
  <span class="pg">5</span>
</section>

<!-- 6 Stats -->
<section class="slide" style="left:696px;top:228px">
  <span class="a gold-v" style="left:1px;top:10px;width:4px;height:51px"></span>
  <div class="a h" style="left:16px;top:11px;font-size:13px;line-height:16px">Lorem<br>Dolor Sit<br>Consectetuer</div>
  <div class="a" style="left:179px;top:36px;width:55px">
    <div style="color:var(--gold);font-weight:800;font-size:10px">768K</div>
    <div style="font-weight:700;font-size:5.5px">Lorem Ipsum</div>
    <p class="tiny">Lorem ipsum dolor sit amet, consectetuer elit.</p>
  </div>
  <div class="a" style="left:246px;top:36px;width:55px">
    <div style="color:var(--gold);font-weight:800;font-size:10px">423K</div>
    <div style="font-weight:700;font-size:5.5px">Lorem Ipsum</div>
    <p class="tiny">Lorem ipsum dolor sit amet, consectetuer elit.</p>
  </div>
  <p class="a tiny" style="left:17px;top:72px;width:128px">Lorem ipsum dolor sit amet, consectetuer adipiscing elit, sed diam nonummy nibh euismod tincidunt ut laoreet dolore magna aliquam erat volutpat.Ut wisi enim ad minim veniam, quis nostrud exerci tation ullamcorper suscipit</p>
  <div class="a gold-h" style="left:175px;top:92px;width:133px;height:21px;color:#fff;font-weight:700;font-size:9.5px;display:flex;align-items:center;padding-left:9px">Text Added Here</div>
  <span class="a gold-v" style="left:69px;top:113px;width:6px;height:61px"></span>
  <div class="photo" role="img" aria-label="Photo of a presenter at a whiteboard with a seated team" style="left:75px;top:113px;width:214px;height:61px;background:linear-gradient(90deg,#dfe3e6 0%,#9aa3aa 40%,#eef0f2 100%)"></div>
  <span class="pg">6</span>
</section>

<!-- 7 Bar chart -->
<section class="slide" style="left:47px;top:417px">
  <div class="a h" style="left:16px;top:13px;font-size:10.5px;line-height:12.5px">Text<br>Added Hare</div>
  <div class="rule" style="left:16px;top:42px"></div>
  <div class="a gold" style="left:0;top:52px;width:99px;height:102px"></div>
  <div class="num-row" style="top:60px"><span class="num-box">1.</span><div><b>Lorem ipsum</b><p class="tiny-w">Lorem ipsum dolor sit amet, consectetuer adipiscing elit, sed diam nonummy nibh euismod tincid</p></div></div>
  <div class="num-row" style="top:92px"><span class="num-box">2.</span><div><b>Lorem ipsum</b><p class="tiny-w">Lorem ipsum dolor sit amet, consectetuer adipiscing elit, sed diam nonummy nibh euismod tincid</p></div></div>
  <div class="num-row" style="top:124px"><span class="num-box">3.</span><div><b>Lorem ipsum</b><p class="tiny-w">Lorem ipsum dolor sit amet, consectetuer adipiscing elit, sed diam nonummy nibh euismod tincid</p></div></div>
  <svg width="308" height="174" viewBox="0 0 308 174" font-family="Montserrat, sans-serif" font-size="4" fill="#333" text-anchor="middle">
    <line x1="108" y1="129" x2="290" y2="129" stroke="#ccc" stroke-width=".5"/>
    <rect x="122" y="56" width="5" height="73" fill="#2a2a2a"/><rect x="128" y="88" width="5" height="41" fill="#a8782f"/><rect x="134" y="95" width="5" height="34" fill="#d8b66a"/>
    <text x="124.5" y="54">43%</text><text x="130.5" y="86">24%</text><text x="136.5" y="93">20%</text>
    <rect x="168" y="86" width="5" height="43" fill="#2a2a2a"/><rect x="174" y="54" width="5" height="75" fill="#a8782f"/><rect x="180" y="95" width="5" height="34" fill="#d8b66a"/>
    <text x="170.5" y="84">25%</text><text x="176.5" y="52">44%</text><text x="182.5" y="93">20%</text>
    <rect x="214" y="69" width="5" height="60" fill="#2a2a2a"/><rect x="220" y="98" width="5" height="31" fill="#a8782f"/><rect x="226" y="78" width="5" height="51" fill="#d8b66a"/>
    <text x="216.5" y="67">35%</text><text x="222.5" y="96">18%</text><text x="228.5" y="76">30%</text>
    <rect x="260" y="52" width="5" height="77" fill="#2a2a2a"/><rect x="266" y="81" width="5" height="48" fill="#a8782f"/><rect x="272" y="44" width="5" height="85" fill="#d8b66a"/>
    <text x="262.5" y="50">45%</text><text x="268.5" y="79">28%</text><text x="274.5" y="42">50%</text>
    <text x="130" y="137">1</text><text x="176" y="137">2</text><text x="222" y="137">3</text><text x="268" y="137">4</text>
    <g font-size="3.4" text-anchor="start">
      <rect x="170" y="143.5" width="2" height="2" fill="#2a2a2a"/><text x="173" y="145.5">Series1</text>
      <rect x="190" y="143.5" width="2" height="2" fill="#a8782f"/><text x="193" y="145.5">Series2</text>
      <rect x="210" y="143.5" width="2" height="2" fill="#d8b66a"/><text x="213" y="145.5">Series3</text>
    </g>
  </svg>
  <span class="a gold-v" style="left:303px;top:20px;width:5px;height:133px"></span>
  <span class="pg">7</span>
</section>

<!-- 8 Donuts -->
<section class="slide" style="left:372px;top:417px">
  <span class="a gold-v" style="left:1px;top:20px;width:3px;height:133px"></span>
  <div class="a h" style="left:0;top:13px;width:308px;text-align:center;font-size:10.5px">Text Added Hare</div>
  <span class="a" style="left:140px;top:29px;width:14px;height:1.4px;background:var(--gold)"></span>
  <span class="a" style="left:156px;top:29px;width:4px;height:1.4px;background:var(--gold-light)"></span>
  <p class="a tiny" style="left:56px;top:37px;width:196px;text-align:center">Lorem ipsum dolor sit amet, consectetuer adipiscing elit, sed diam nonummy nibh euismod tincidunt ut laoreet dolore magna aliquam erat volutpat. Ut wisi enim ad minim veniam, quis nostrud exerci tation ullamcorper suscipit lobortis nisl ut aliquip ex ea commodo consequat. Duis autem vel eum iriure</p>
  <svg width="308" height="174" viewBox="0 0 308 174" font-family="Montserrat, sans-serif" text-anchor="middle">
    <g fill="none" stroke-width="3.5">
      <circle cx="75" cy="98" r="25" stroke="#eee"/><circle cx="75" cy="98" r="25" stroke="#2a2a2a" stroke-dasharray="78.5 157" transform="rotate(-90 75 98)"/>
      <circle cx="154" cy="98" r="25" stroke="#eee"/><circle cx="154" cy="98" r="25" stroke="#a8782f" stroke-dasharray="117.8 157" transform="rotate(-90 154 98)"/>
      <circle cx="234" cy="98" r="25" stroke="#eee"/><circle cx="234" cy="98" r="25" stroke="#d8b66a" stroke-dasharray="62.8 157" transform="rotate(-90 234 98)"/>
    </g>
    <g font-size="13" font-weight="500" fill="#1e1e1e">
      <text x="75" y="103">50%</text><text x="154" y="103">75%</text><text x="234" y="103">40%</text>
    </g>
    <g font-size="3.6" fill="#8c8c8c">
      <text x="75" y="136">Lorem ipsum dolor amet amet</text><text x="75" y="140.5">consectetur dolor</text>
      <text x="154" y="136">Lorem ipsum dolor amet amet</text><text x="154" y="140.5">consectetur dolor</text>
      <text x="234" y="136">Lorem ipsum dolor amet amet</text><text x="234" y="140.5">consectetur dolor</text>
    </g>
  </svg>
  <span class="pg">8</span>
</section>

<!-- 9 Cycle diagram -->
<section class="slide" style="left:696px;top:417px">
  <div class="a h" style="left:16px;top:13px;font-size:10.5px;line-height:12.5px">Text<br>Added Hare</div>
  <div class="rule" style="left:16px;top:42px"></div>
  <p class="a tiny" style="left:16px;top:50px;width:90px">Lorem ipsum dolor sit amet, consectetuer adipiscing elit, sed diam nonummy nibh .</p>
  <p class="a tiny" style="left:16px;top:65px;width:90px">Ut wisi enim ad minim veniam, quis nostrud exerci tation ullamcorper suscipit lobortis. Ut wisi enim ad minim veniam, quis nostrud exerci tation ullamcorper suscipit</p>
  <div class="a gold" style="left:0;top:97px;width:99px;height:57px"></div>
  <div class="a" style="left:10px;top:104px;width:84px;color:#fff">
    <div style="font-size:5px;font-weight:700;display:flex;gap:3px;align-items:center"><span style="width:4px;height:4px;border-radius:50%;background:#fff"></span>Lorem Ipsum</div>
    <p class="tiny-w" style="padding-left:7px">Lorem ipsum dolor sit amet, consectetuer adipiscing elit, sed diam nonummy nibh euismod tincidunt ut laoreet</p>
  </div>
  <div class="a" style="left:10px;top:129px;width:84px;color:#fff">
    <div style="font-size:5px;font-weight:700;display:flex;gap:3px;align-items:center"><span style="width:4px;height:4px;border-radius:50%;background:#fff"></span>Lorem Ipsum</div>
    <p class="tiny-w" style="padding-left:7px">Lorem ipsum dolor sit amet, consectetuer adipiscing elit, sed diam nonummy nibh euismod tincidunt ut laoreet</p>
  </div>
  <svg width="308" height="174" viewBox="0 0 308 174" font-family="Montserrat, sans-serif">
    <path d="M229 40 A58 52 0 0 0 141 88" fill="none" stroke="#2a2a2a" stroke-width="2.2"/>
    <path d="M136.5 82 L141 90 L145.5 82" fill="none" stroke="#2a2a2a" stroke-width="2"/>
    <path d="M240 62 Q256 80 243 100 Q232 120 219 132 Q188 146 155 120 L143 105" fill="none" stroke="#2a2a2a" stroke-width="2.2"/>
    <circle cx="143" cy="104" r="2.6" fill="#2a2a2a"/>
    <g>
      <circle cx="232" cy="54" r="17" fill="#c39a45"/><circle cx="232" cy="54" r="11" fill="#fff"/><circle cx="232" cy="54" r="8" fill="#d8b66a"/>
      <circle cx="231" cy="53" r="2.8" fill="none" stroke="#fff" stroke-width="1"/><line x1="233" y1="55" x2="235.5" y2="57.5" stroke="#fff" stroke-width="1"/>
      <circle cx="243" cy="100" r="13" fill="#2a2a2a"/><circle cx="243" cy="100" r="9" fill="#c39a45"/><circle cx="243" cy="100" r="5.5" fill="#fff"/><circle cx="243" cy="99" r="2" fill="#c39a45"/>
      <circle cx="219" cy="132" r="10" fill="#c39a45"/><circle cx="219" cy="132" r="6.5" fill="#fff"/><line x1="219" y1="129" x2="219" y2="135" stroke="#a8782f" stroke-width="1"/><path d="M216 133 Q219 136 222 133" fill="none" stroke="#a8782f" stroke-width=".8"/>
      <circle cx="155" cy="120" r="10" fill="#c39a45"/><circle cx="155" cy="120" r="6.5" fill="#fff"/><circle cx="155" cy="120" r="3" fill="#d8b66a"/>
    </g>
    <rect x="173" y="71" width="2" height="6" fill="#a8782f"/><rect x="176" y="68" width="2" height="9" fill="#a8782f"/><rect x="179" y="72" width="2" height="5" fill="#a8782f"/><rect x="171" y="77" width="12" height=".8" fill="#a8782f"/>
    <text x="177" y="84" text-anchor="middle" font-size="5" font-weight="600" fill="#1e1e1e">MAIN TITLE</text>
    <text x="177" y="88" text-anchor="middle" font-size="2.5" fill="#777">Lorem ipsum dolor sit amet,</text>
    <text x="177" y="91" text-anchor="middle" font-size="2.5" fill="#777">consectetuer adipiscing elit</text>
    <g font-size="3.2" font-style="italic" font-weight="700" fill="#1e1e1e">
      <text x="251" y="38">85%</text><text x="212" y="88">80%</text><text x="178" y="117">50%</text><text x="238" y="144">75%</text>
    </g>
    <g font-size="4.2" font-weight="600" fill="#1e1e1e" text-anchor="end">
      <text x="294" y="47">Your Title</text><text x="294" y="92">Your Title</text><text x="294" y="130">Your Title</text>
      <text x="145" y="120">Your Title</text>
    </g>
    <g font-size="2.5" fill="#777" text-anchor="end">
      <text x="294" y="51">Lorem ipsum dolor sit amet,</text><text x="294" y="54">consectetuer adipiscing</text>
      <text x="294" y="96">Lorem ipsum dolor sit amet,</text><text x="294" y="99">consectetuer adipiscing</text>
      <text x="294" y="134">Lorem ipsum dolor sit amet,</text><text x="294" y="137">consectetuer adipiscing</text>
      <text x="145" y="124">Lorem ipsum dolor sit amet,</text><text x="145" y="127">consectetuer adipiscing</text>
    </g>
  </svg>
  <span class="a gold-v" style="left:303px;top:20px;width:5px;height:133px"></span>
  <span class="pg">9</span>
</section>

<!-- 10 Service -->
<section class="slide" style="left:47px;top:605px">
  <span class="a gold" style="left:0;top:0;width:55px;height:50px"></span>
  <div class="photo" role="img" aria-label="Photo of two business colleagues looking at a tablet" style="left:19px;top:19px;width:116px;height:135px;background:linear-gradient(135deg,#eef0f2 0%,#9aa3ac 50%,#2c3440 100%)"></div>
  <div class="a gold-h" style="left:43px;top:135px;width:68px;height:19px;color:#fff;font-weight:700;font-size:10px;display:flex;align-items:center;justify-content:center">Service</div>
  <svg width="308" height="174" viewBox="0 0 308 174">
    <g id="target-10">
      <circle cx="164" cy="43" r="12" fill="#d8b66a"/><circle cx="164" cy="43" r="7" fill="none" stroke="#fff" stroke-width=".8"/><circle cx="164" cy="43" r="4" fill="none" stroke="#fff" stroke-width=".8"/><circle cx="164" cy="43" r="1.2" fill="#fff"/>
      <circle cx="164" cy="88" r="12" fill="#d8b66a"/><circle cx="164" cy="88" r="7" fill="none" stroke="#fff" stroke-width=".8"/><circle cx="164" cy="88" r="4" fill="none" stroke="#fff" stroke-width=".8"/><circle cx="164" cy="88" r="1.2" fill="#fff"/>
      <circle cx="164" cy="133" r="12" fill="#d8b66a"/><circle cx="164" cy="133" r="7" fill="none" stroke="#fff" stroke-width=".8"/><circle cx="164" cy="133" r="4" fill="none" stroke="#fff" stroke-width=".8"/><circle cx="164" cy="133" r="1.2" fill="#fff"/>
    </g>
  </svg>
  <div class="icon-row" style="left:183px;top:34px"><div><b>Project name</b><p class="tiny">Lorem ipsum dolor sit amet. nec an dictas equidem appellantur, ut has commune accommodare. Mea illum, ludus solet idpro.</p></div></div>
  <div class="icon-row" style="left:183px;top:79px"><div><b>Project name</b><p class="tiny">Lorem ipsum dolor sit amet. nec an dictas equidem appellantur, ut has commune accommodare. Mea illum, ludus solet idpro.</p></div></div>
  <div class="icon-row" style="left:183px;top:124px"><div><b>Project name</b><p class="tiny">Lorem ipsum dolor sit amet. nec an dictas equidem appellantur, ut has commune accommodare. Mea illum, ludus solet idpro.</p></div></div>
  <span class="a gold-v" style="left:303px;top:21px;width:5px;height:131px"></span>
  <span class="pg">10</span>
</section>

<!-- 11 SWOT -->
<section class="slide" style="left:372px;top:605px">
  <div class="a h" style="left:13px;top:10px;font-size:10.5px">Text Added Hare</div>
  <div class="rule" style="left:13px;top:26px"></div>
  <svg width="308" height="174" viewBox="0 0 308 174" font-family="Montserrat, sans-serif" text-anchor="middle">
    <line x1="155" y1="40" x2="155" y2="148" stroke="#bbb" stroke-width=".7" stroke-dasharray="1 1.5"/>
    <line x1="102" y1="93" x2="210" y2="93" stroke="#bbb" stroke-width=".7" stroke-dasharray="1 1.5"/>
    <circle cx="132" cy="70" r="20" fill="#a8782f"/><circle cx="179" cy="70" r="20" fill="#d8b66a"/>
    <circle cx="132" cy="117" r="20" fill="#d8b66a"/><circle cx="179" cy="117" r="20" fill="#a8782f"/>
    <circle cx="155" cy="93" r="17" fill="#2a2a2a"/>
    <g font-size="17" font-weight="500" fill="#fff" font-style="italic">
      <text x="132" y="76">S</text><text x="179" y="76">W</text><text x="132" y="123">O</text><text x="179" y="123">T</text>
    </g>
    <text x="155" y="95" font-size="4.5" font-style="italic" font-weight="500" fill="#fff">ANALYSIS</text>
  </svg>
  <div class="swot-label" style="left:76px;top:40px">STRENGTHS<ul><li>• Good location</li><li>• Very affordable prices</li><li>• Variety of activities</li><li>• Personal trainer</li></ul></div>
  <div class="swot-label" style="left:203px;top:38px">WEAKNESSES<ul><li>• Not many promotions</li><li>&nbsp; during the year</li><li>• Small fitness</li><li>&nbsp; training rooms</li><li>• Presence in social</li><li>&nbsp; networks can be improved</li></ul></div>
  <div class="swot-label" style="left:73px;top:105px">OPPORTUNITIES<ul><li>• Hiring more graphic</li><li>&nbsp; designers and staff</li><li>• An app can be practical</li><li>&nbsp; to track results and</li><li>&nbsp; view workout statistics</li></ul></div>
  <div class="swot-label" style="left:206px;top:105px">THREATS<ul><li>• Other gyms have more</li><li>&nbsp; space to workout</li><li>• There are many free</li><li>&nbsp; fitness apps</li><li>• Principal competitors</li><li>&nbsp; have nutritionist</li></ul></div>
  <span class="a gold-v" style="left:303px;top:21px;width:5px;height:131px"></span>
  <span class="pg">11</span>
</section>

<!-- 12 Hub -->
<section class="slide" style="left:696px;top:605px">
  <svg width="308" height="174" viewBox="0 0 308 174" font-family="Montserrat, sans-serif" text-anchor="middle">
    <circle cx="68" cy="86" r="41" fill="#fff" stroke="#2a2a2a" stroke-width="3"/>
    <circle cx="68" cy="86" r="36" fill="none" stroke="#ccc" stroke-width=".8"/>
    <defs><linearGradient id="hub-gold" x1="0" y1="0" x2="1" y2="1"><stop offset="0" stop-color="#efdc98"/><stop offset=".5" stop-color="#c39a45"/><stop offset="1" stop-color="#8a5a1c"/></linearGradient></defs>
    <circle cx="68" cy="86" r="33" fill="url(#hub-gold)"/>
    <g font-size="10" font-weight="700" fill="#fff"><text x="68" y="78">Text</text><text x="68" y="90">Added</text><text x="68" y="102">Hare</text></g>
    <polyline points="109,63 125,43 153,43" fill="none" stroke="#555" stroke-width=".6"/>
    <line x1="116" y1="86" x2="150" y2="86" stroke="#555" stroke-width=".6"/>
    <polyline points="109,109 125,129 153,129" fill="none" stroke="#555" stroke-width=".6"/>
    <g>
      <circle cx="171" cy="44" r="12" fill="#d8b66a"/><circle cx="171" cy="44" r="7" fill="none" stroke="#fff" stroke-width=".8"/><circle cx="171" cy="44" r="4" fill="none" stroke="#fff" stroke-width=".8"/><circle cx="171" cy="44" r="1.2" fill="#fff"/>
      <circle cx="171" cy="86" r="12" fill="#d8b66a"/><circle cx="171" cy="86" r="7" fill="none" stroke="#fff" stroke-width=".8"/><circle cx="171" cy="86" r="4" fill="none" stroke="#fff" stroke-width=".8"/><circle cx="171" cy="86" r="1.2" fill="#fff"/>
      <circle cx="171" cy="128" r="12" fill="#d8b66a"/><circle cx="171" cy="128" r="7" fill="none" stroke="#fff" stroke-width=".8"/><circle cx="171" cy="128" r="4" fill="none" stroke="#fff" stroke-width=".8"/><circle cx="171" cy="128" r="1.2" fill="#fff"/>
    </g>
  </svg>
  <div class="icon-row" style="left:191px;top:35px"><div><b>Project name</b><p class="tiny">Lorem ipsum dolor sit amet. nec an dictas equidem appellantur, ut has commune accommodare. Mea illum, ludus solet idpro.</p></div></div>
  <div class="icon-row" style="left:191px;top:77px"><div><b>Project name</b><p class="tiny">Lorem ipsum dolor sit amet. nec an dictas equidem appellantur, ut has commune accommodare. Mea illum, ludus solet idpro.</p></div></div>
  <div class="icon-row" style="left:191px;top:119px"><div><b>Project name</b><p class="tiny">Lorem ipsum dolor sit amet. nec an dictas equidem appellantur, ut has commune accommodare. Mea illum, ludus solet idpro.</p></div></div>
  <span class="pg">12</span>
</section>

<!-- 13 Timeline -->
<section class="slide" style="left:47px;top:792px">
  <div class="a gold-h" style="left:0;top:13px;width:161px;height:18px;color:#fff;font-weight:800;font-size:10.5px;display:flex;align-items:center;padding-left:15px">Project Timeline - 2024</div>
  <svg width="308" height="174" viewBox="0 0 308 174" font-family="Montserrat, sans-serif" text-anchor="middle">
    <polygon points="38,91 76,91 80,100 34,100" fill="#d8b66a"/>
    <polygon points="80,91 126,91 122,100 84,100" fill="#9a6a24"/>
    <polygon points="130,91 168,91 172,100 126,100" fill="#d8b66a"/>
    <polygon points="172,91 218,91 214,100 176,100" fill="#9a6a24"/>
    <polygon points="222,91 260,91 264,100 218,100" fill="#d8b66a"/>
    <g font-size="3.8" font-weight="600" fill="#fff">
      <text x="57" y="97.3">1990</text><text x="103" y="97.3">2001</text><text x="149" y="97.3">2007</text><text x="195" y="97.3">2012</text><text x="241" y="97.3">2020</text>
    </g>
    <g stroke="#a8782f" stroke-width=".8">
      <line x1="57" y1="78" x2="57" y2="89"/><line x1="149" y1="78" x2="149" y2="89"/><line x1="241" y1="78" x2="241" y2="89"/>
      <line x1="103" y1="102" x2="103" y2="113"/><line x1="195" y1="102" x2="195" y2="113"/>
    </g>
    <g fill="#a8782f">
      <circle cx="57" cy="78" r="1.3"/><circle cx="149" cy="78" r="1.3"/><circle cx="241" cy="78" r="1.3"/>
      <circle cx="103" cy="113" r="1.3"/><circle cx="195" cy="113" r="1.3"/>
    </g>
  </svg>
  <div class="tl-label" style="left:57px;top:55px">Your Title<span>Refers to a good or service being offered</span></div>
  <div class="tl-label" style="left:149px;top:55px">Your Title<span>Refers to a good or service being offered</span></div>
  <div class="tl-label" style="left:241px;top:55px">Your Title<span>Refers to a good or service being offered</span></div>
  <div class="tl-label" style="left:103px;top:123px">Your Title<span>Refers to a good or service being offered</span></div>
  <div class="tl-label" style="left:195px;top:123px">Your Title<span>Refers to a good or service being offered</span></div>
  <span class="pg">13</span>
</section>

<!-- 14 Buttons -->
<section class="slide" style="left:372px;top:792px">
  <div class="photo" role="img" aria-label="Dark photo of a hand with a glowing network overlay" style="left:0;top:0;width:108px;height:174px;background:linear-gradient(160deg,#3a3a3a 0%,#2a2a2a 50%,#1c1c1c 100%)"></div>
  <div class="a" style="left:22px;top:28px;height:120px;display:flex;align-items:center">
    <span style="writing-mode:vertical-rl;color:#fff;font-weight:700;font-size:11px;letter-spacing:3px">TEXT ADDED</span>
  </div>
  <div class="btn gold-h" style="top:28px">1. Lorem Ipsum</div>
  <div class="btn gold-h" style="top:73px">2. Lorem Ipsum</div>
  <div class="btn gold-h" style="top:124px">3. Lorem Ipsum</div>
  <div class="a h" style="left:189px;top:49px;font-size:10.5px;line-height:13px">Text<br>Added Hare</div>
  <div class="rule" style="left:189px;top:79px"></div>
  <p class="a tiny" style="left:189px;top:86px;width:92px">Lorem ipsum dolor sit amet, consectetuer adipiscing elit, sed diam nonummy nibh .</p>
  <p class="a tiny" style="left:189px;top:99px;width:92px">Ut wisi enim ad minim veniam, quis nostrud exerci tation ullamcorper suscipit lobortis. Ut wisi enim ad minim veniam, quis nostrud exerci tation ullamcorper suscipit</p>
  <span class="pg">14</span>
</section>

<!-- 15 Steps -->
<section class="slide" style="left:696px;top:792px">
  <div class="a h" style="left:13px;top:10px;font-size:10.5px">Text Added Hare</div>
  <div class="rule" style="left:13px;top:26px"></div>
  <svg width="308" height="174" viewBox="0 0 308 174" font-family="Montserrat, sans-serif" text-anchor="middle">
    <defs><linearGradient id="step-band" x1="0" x2="1"><stop offset="0" stop-color="#9a6a24"/><stop offset=".5" stop-color="#c39a45"/><stop offset="1" stop-color="#e6cf86"/></linearGradient></defs>
    <rect x="20" y="92" width="254" height="5" fill="url(#step-band)"/>
    <path d="M272 89 L280 94.5 L272 100 Z" fill="#e6cf86"/>
    <g fill="none" stroke-width="4">
      <path d="M58 90 A16 16 0 1 1 82 90" stroke="#a8782f"/>
      <path d="M113 90 A16 16 0 1 1 137 90" stroke="#c39a45"/>
      <path d="M167 90 A16 16 0 1 1 191 90" stroke="#b8893a"/>
      <path d="M221 90 A16 16 0 1 1 245 90" stroke="#d8b66a"/>
    </g>
    <g fill="#fff"><circle cx="70" cy="77" r="11"/><circle cx="125" cy="77" r="11"/><circle cx="179" cy="77" r="11"/><circle cx="233" cy="77" r="11"/></g>
    <circle cx="70" cy="77" r="6" fill="none" stroke="#2a2a2a" stroke-width="1"/><path d="M70 73.5 V77 L72.5 78.5" fill="none" stroke="#2a2a2a" stroke-width="1"/>
    <circle cx="125" cy="78" r="5" fill="#2a2a2a"/><text x="125" y="80" font-size="5.5" font-weight="700" fill="#fff">$</text>
    <g fill="none" stroke="#2a2a2a" stroke-width=".9"><ellipse cx="179" cy="73.5" rx="5" ry="1.6"/><path d="M174 73.5 V80.5 A5 1.6 0 0 0 184 80.5 V73.5"/><path d="M174 77 A5 1.6 0 0 0 184 77"/></g>
    <circle cx="234" cy="76" r="3.6" fill="none" stroke="#2a2a2a" stroke-width="1.1"/><line x1="231.5" y1="78.5" x2="228.5" y2="81.5" stroke="#2a2a2a" stroke-width="1.4"/>
    <g font-size="3.4" font-weight="600" fill="#fff"><text x="82" y="95.6">Step 01</text><text x="137" y="95.6">Step 02</text><text x="190" y="95.6">Step 03</text><text x="253" y="95.6">Step 04</text></g>
    <g stroke="#777" stroke-width=".6"><line x1="70" y1="99" x2="70" y2="108"/><line x1="125" y1="99" x2="125" y2="108"/><line x1="179" y1="99" x2="179" y2="108"/><line x1="233" y1="99" x2="233" y2="108"/></g>
  </svg>
  <div class="step" style="left:70px;top:111px"><b>Lorem Ipsum</b><p class="tiny">Lorem ipsum dolor sit amet, consectetuer adipiscing elit, sed diam nonummy nibh euismod tincidunt ut laoreet dolore magna aliquam erat</p></div>
  <div class="step" style="left:125px;top:111px"><b>Lorem Ipsum</b><p class="tiny">Lorem ipsum dolor sit amet, consectetuer adipiscing elit, sed diam nonummy nibh euismod tincidunt ut laoreet dolore magna aliquam erat</p></div>
  <div class="step" style="left:179px;top:111px"><b>Lorem Ipsum</b><p class="tiny">Lorem ipsum dolor sit amet, consectetuer adipiscing elit, sed diam nonummy nibh euismod tincidunt ut laoreet dolore magna aliquam erat</p></div>
  <div class="step" style="left:233px;top:111px"><b>Lorem Ipsum</b><p class="tiny">Lorem ipsum dolor sit amet, consectetuer adipiscing elit, sed diam nonummy nibh euismod tincidunt ut laoreet dolore magna aliquam erat</p></div>
  <span class="pg">15</span>
</section>

<!-- 16 Mobile -->
<section class="slide" style="left:47px;top:981px">
  <div class="a h" style="left:20px;top:18px;font-size:15px;line-height:19.5px">Text<br><span class="hl">Added</span><br>Here</div>
  <div class="a gold" style="left:0;top:88px;width:115px;height:67px"></div>
  <div class="num-row" style="top:95px"><span class="num-box">1.</span><div><b>Lorem Ipsum</b><p class="tiny-w">Lorem ipsum dolor sit amet, consectetuer adipiscing elit, sed diam nonummy nibh euismod</p></div></div>
  <div class="num-row" style="top:116px"><span class="num-box">2.</span><div><b>Lorem Ipsum</b><p class="tiny-w">Lorem ipsum dolor sit amet, consectetuer adipiscing elit, sed diam nonummy nibh euismod</p></div></div>
  <div class="num-row" style="top:137px"><span class="num-box">3.</span><div><b>Lorem Ipsum</b><p class="tiny-w">Lorem ipsum dolor sit amet, consectetuer adipiscing elit, sed diam nonummy nibh euismod</p></div></div>
  <div class="photo" role="img" aria-label="Faint world map in the background" style="left:122px;top:45px;width:174px;height:81px;background:radial-gradient(ellipse at 50% 50%,#efefef 0%,#f6f6f6 60%,#ffffff 100%)"></div>
  <div class="phone" style="left:139px;top:26px"><b>Lorem<br>ipsum dolor</b><i></i><p class="tiny">To introduce the team to the changing landscape of marketing and equip them with knowledge and tools.</p></div>
  <div class="phone" style="left:186px;top:49px"><b>Dolor sit<br>amet, conse</b><i></i><p class="tiny">You will learn concepts and ideas in digital marketing as well as how to use different tools.</p></div>
  <div class="phone" style="left:233px;top:75px"><b>Consec</b><i></i><p class="tiny">You are required to pass 80% of the evaluation test to obtain the certificate.</p></div>
  <span class="pg">22</span>
</section>

<!-- 17 Team -->
<section class="slide" style="left:372px;top:981px">
  <div class="a gold" style="left:0;top:19px;width:308px;height:61px"></div>
  <div class="a" style="left:0;top:35px;width:308px;text-align:center;color:#fff;font-weight:700;font-size:14px">The Team Members</div>
  <div class="member" style="left:51px;top:66px"><div class="avatar" role="img" aria-label="Portrait photo of team member"></div><b>ARON VALE</b><p class="tiny">Ipsum dolor sit amet, cons ectetuer adipiscing elit, sed diam nonummy nibh euismod tincidunt<br><br>ut laoreet dolore magna aliquam erat volut. Ut wisi enim ad minim veniam, quis nostrud</p></div>
  <div class="member" style="left:118px;top:66px"><div class="avatar" role="img" aria-label="Portrait photo of team member"></div><b>MIRA HOLT</b><p class="tiny">Ipsum dolor sit amet, cons ectetuer adipiscing elit, sed diam nonummy nibh euismod tincidunt<br><br>ut laoreet dolore magna aliquam erat volut. Ut wisi enim ad minim veniam, quis nostrud</p></div>
  <div class="member" style="left:187px;top:66px"><div class="avatar" role="img" aria-label="Portrait photo of team member"></div><b>ARON VALE</b><p class="tiny">Ipsum dolor sit amet, cons ectetuer adipiscing elit, sed diam nonummy nibh euismod tincidunt<br><br>ut laoreet dolore magna aliquam erat volut. Ut wisi enim ad minim veniam, quis nostrud</p></div>
  <div class="member" style="left:257px;top:66px"><div class="avatar" role="img" aria-label="Portrait photo of team member"></div><b>MIRA HOLT</b><p class="tiny">Ipsum dolor sit amet, cons ectetuer adipiscing elit, sed diam nonummy nibh euismod tincidunt<br><br>ut laoreet dolore magna aliquam erat volut. Ut wisi enim ad minim veniam, quis nostrud</p></div>
  <span class="pg">23</span>
</section>

<!-- 18 Thank you -->
<section class="slide" style="left:698px;top:981px">
  <div class="a logo" style="left:166px;top:32px;font-size:8px"><span class="logo-dot"></span>Tidal Forge MSP</div>
  <div class="a h" style="left:20px;top:45px;font-size:18px;font-weight:700">Thank You</div>
  <svg width="308" height="174" viewBox="0 0 308 174">
    <path d="M21 76 q1-2 3-2 l2 3 -1.5 1.5 q1 3 4 4.5 l1.5-1.5 3 2 q0 2-2 3 q-6 0-10-10z" fill="#a8782f"/>
    <path d="M21 95 L33 90 L28 102 L26.5 97 Z" fill="#a8782f"/>
    <path d="M21 117 L27 111.5 L33 117 H31 V122 H28.5 V118.5 H25.5 V122 H23 V117 Z" fill="#a8782f"/>
  </svg>
  <div class="contact" style="top:75px;left:35px"><span class="sep"></span><span>+1 555 0142 7788<br>+1 555 0142 7788</span></div>
  <div class="contact" style="top:94px;left:35px"><span class="sep"></span><span>www.tidalforge.com<br>hello@tidalforge.com</span></div>
  <div class="contact" style="top:111px;left:35px"><span class="sep"></span><span>88 Harbor Lane, Port Ellis,<br>CA 90210, USA</span></div>
</section>

</body>
</html>
```